Quillory Nest Business Card

I need a business card design. We are a collaborate online training company. Our colors are gray and green. Our website is QuilloryNest.com

I would like an area for a profile picture within the card

```html
<!DOCTYPE html>
<html lang="en">
<head>
<meta charset="utf-8">
<title>Quillory Nest Business Card</title>
<link rel="stylesheet" href="https://fonts.googleapis.com/css2?family=Lato:wght@400;700;900&display=swap">
<style>
  :root {
    --green: #8dc63f;
    --green-dark: #6fa62a;
    --ink: #111111;
    --gray-text: #2b2b2b;
    --paper: #ffffff;
    --paper-shade: #ececec;
    --backdrop: #3a3a3a;
    --photo-light: #c9c9c9;
    --photo-dark: #5a5a5a;
  }
  * { box-sizing: border-box; margin: 0; padding: 0; }
  html, body { width: 1200px; height: 800px; overflow: hidden; }
  body {
    background: var(--backdrop);
    font-family: "Lato", Arial, sans-serif;
    position: relative;
  }
  .card {
    position: absolute;
    top: 246px;
    width: 540px;
    height: 308px;
    border-radius: 14px;
    overflow: hidden;
    box-shadow: 0 10px 24px rgba(0,0,0,0.45);
  }
  .card-front { left: 40px; background: var(--green); }
  .card-back {
    left: 620px;
    background: linear-gradient(180deg, var(--paper-shade) 0%, var(--paper) 60%);
  }

  /* front */
  .brand {
    display: flex;
    align-items: center;
    gap: 12px;
    font-weight: 900;
    letter-spacing: -0.5px;
  }
  .brand-dot { border-radius: 50%; flex: none; }
  .card-front .brand {
    position: absolute;
    left: 0; right: 0; top: 50%;
    transform: translateY(-50%);
    justify-content: center;
    color: var(--paper);
    font-size: 46px;
  }
  .card-front .brand-dot { width: 40px; height: 40px; background: var(--paper); }

  /* back */
  .card-back .brand {
    position: absolute;
    left: 32px; top: 40px;
    color: var(--ink);
    font-size: 30px;
  }
  .card-back .brand-dot { width: 28px; height: 28px; background: var(--green); }

  .portrait {
    position: absolute;
    right: 34px; top: 0;
    width: 190px; height: 210px;
    background: linear-gradient(160deg, var(--photo-light) 0%, var(--photo-dark) 100%);
  }

  .contact {
    position: absolute;
    left: 34px; top: 128px;
    color: var(--gray-text);
    font-size: 13px;
    line-height: 1.35;
  }
  .address { margin-bottom: 12px; }
  .contact-list { list-style: none; }
  .contact-list li { display: flex; align-items: center; gap: 8px; }
  .contact-list svg { width: 12px; height: 12px; flex: none; }

  .wave { position: absolute; left: 0; top: 0; width: 540px; height: 308px; }

  .person {
    position: absolute;
    right: 28px; top: 222px;
    text-align: right;
    color: var(--ink);
  }
  .person-name { font-weight: 900; font-size: 22px; line-height: 1.1; }
  .person-role { font-size: 15px; }
</style>
</head>
<body>

  <section class="card card-front">
    <div class="brand"><span class="brand-dot"></span>Quillory Nest</div>
  </section>

  <section class="card card-back">
    <div class="brand"><span class="brand-dot"></span>Quillory Nest</div>

    <div class="portrait" role="img" aria-label="Profile photograph of the founder"></div>

    <svg class="wave" viewBox="0 0 540 308" aria-hidden="true">
      <path d="M0,246 C150,286 260,226 330,196 C400,166 470,148 540,148 L540,308 L0,308 Z" fill="var(--ink)"/>
      <path d="M0,262 C150,302 260,242 330,212 C400,182 470,164 540,164 L540,308 L0,308 Z" fill="var(--green)"/>
    </svg>

    <div class="contact">
      <p class="address">418 E Harlow Ave<br>Suite 7 Brennick, Arizona 85390</p>
      <ul class="contact-list">
        <li>
          <svg viewBox="0 0 12 12"><path d="M2 1h3l1 3-2 1a6 6 0 0 0 3 3l1-2 3 1v3c-6 1-10-3-9-9z" fill="var(--green-dark)"/></svg>
          (555) 204-7731
        </li>
        <li>
          <svg viewBox="0 0 12 12"><rect x="0.5" y="2" width="11" height="8" fill="var(--green-dark)"/><path d="M0.5 2l5.5 4.5L11.5 2" stroke="#fff" fill="none"/></svg>
          dalen@quillorynest.com
        </li>
        <li>
          <svg viewBox="0 0 12 12"><circle cx="6" cy="6" r="5.5" fill="var(--green-dark)"/><path d="M0.5 6h11M6 0.5v11M2 3h8M2 9h8" stroke="#fff" stroke-width="0.8"/></svg>
          www.quillorynest.com
        </li>
      </ul>
    </div>

    <div class="person">
      <p class="person-name">Dalen Marsh</p>
      <p class="person-role">Founder</p>
    </div>
  </section>

</body>
</html>
```